Make a Facebook/Instagram ad

Design a facebook/instagram ad. Use info from our website, www.corvantsatellite.com Make ad Alaska themed summer
Ad
Upgrade to Corvant
New BRISK internet packages starting at only $69.99!
Coverage to most areas of the Southern Kenai Peninsula
Low latency fiberoptic based connection , not satellite

```html
<!DOCTYPE html>
<html lang="en">
<head>
<meta charset="UTF-8">
<title>Upgrade to Corvant – BRISK Internet</title>
<link rel="stylesheet" href="https://fonts.googleapis.com/css2?family=Roboto+Condensed:ital,wght@0,700;0,900;1,400;1,700&family=Roboto:ital,wght@1,500&family=Questrial&display=swap">
<style>
  :root {
    --ink: #0b0b0b;
    --paper: #ffffff;
    --sky: #4a9fd8;
    --sky-pale: #a9d2ee;
    --forest: #2c3f2a;
    --sea: #4fa6a8;
  }
  * { margin: 0; padding: 0; box-sizing: border-box; }
  html, body { width: 960px; height: 1200px; overflow: hidden; background: var(--paper); }
  .ad {
    position: relative;
    width: 960px;
    height: 1200px;
    overflow: hidden;
    font-family: "Roboto Condensed", "Arial Narrow", sans-serif;
  }
  .scene {
    position: absolute;
    inset: 0;
    background: linear-gradient(180deg,
      var(--sky) 0%,
      var(--sky-pale) 42%,
      var(--forest) 60%,
      var(--forest) 80%,
      var(--sea) 92%,
      var(--sea) 100%);
  }
  .headline {
    position: absolute;
    left: 66px;
    top: 50px;
    display: flex;
    align-items: baseline;
    color: var(--ink);
    white-space: nowrap;
  }
  .headline-lead {
    font-weight: 700;
    font-size: 80px;
    letter-spacing: -1px;
  }
  .headline-brand {
    font-family: "Roboto", "Helvetica", sans-serif;
    font-style: italic;
    font-weight: 500;
    font-size: 112px;
    letter-spacing: -3px;
    margin-left: 12px;
  }
  .offer {
    position: absolute;
    left: 67px;
    top: 212px;
    font-style: italic;
    font-weight: 400;
    font-size: 59px;
    line-height: 50px;
    color: var(--ink);
    letter-spacing: -0.5px;
  }
  .offer strong { font-weight: 700; }
  .price {
    position: absolute;
    left: 60px;
    top: 330px;
    font-weight: 900;
    font-size: 160px;
    line-height: 1;
    letter-spacing: -5px;
    color: var(--ink);
  }
  .features {
    position: absolute;
    left: 67px;
    top: 672px;
    list-style: none;
    font-family: "Questrial", "Helvetica", sans-serif;
    font-size: 43px;
    line-height: 54px;
    color: var(--paper);
    text-transform: uppercase;
    letter-spacing: -0.5px;
  }
  .features li + li { margin-top: 23px; }
  .product-name {
    position: absolute;
    left: 67px;
    top: 1020px;
    font-family: "Questrial", "Helvetica", sans-serif;
    font-size: 130px;
    line-height: 1;
    color: var(--paper);
  }
  .company-name {
    position: absolute;
    left: 480px;
    top: 1086px;
    display: flex;
    align-items: center;
    gap: 14px;
    font-weight: 700;
    font-size: 54px;
    color: var(--paper);
    letter-spacing: -0.5px;
  }
  .company-dot {
    width: 20px;
    height: 20px;
    border-radius: 50%;
    background: var(--paper);
  }
</style>
</head>
<body>
  <main class="ad">
    <div class="scene" role="img" aria-label="Photo of an Alaskan fjord in summer: snow-capped mountains under a blue sky, a forested cliff and turquoise water with floating ice"></div>

    <h1 class="headline">
      <span class="headline-lead">Upgrade to</span>
      <span class="headline-brand">Corvant</span>
    </h1>

    <p class="offer">New <strong>BRISK</strong> internet packages<br>starting at only</p>

    <p class="price">$69.99</p>

    <ul class="features">
      <li>Coverage to most areas of<br>the Southern Kenai Peninsula</li>
      <li>Low latency fiberoptic based<br>connection, not satellite</li>
    </ul>

    <p class="product-name">BRISK</p>

    <div class="company-name">
      <span class="company-dot"></span>
      <span>Corvant Satellite</span>
    </div>
  </main>
</body>
</html>
```